Dalton Power Supply, Inc. Business Card Design

We are an Electrical Distributor looking for a Modern, Professional Business Card design.

Target Market(s)

Residential Commercial Industrial

Industry/Entity Type

Electrical

Contact Information for Business Card

Dalton Power Supply, Inc.
418 Maple Ridge Lane
Brookvale, NC 27514
555-214-7630
555-214-8842 Fax
daltonpower@brightmail-example.net

```html
<!DOCTYPE html>
<html lang="en">
<head>
<meta charset="utf-8">
<title>Dalton Power Supply, Inc. – Business Card</title>
<link rel="stylesheet" href="https://fonts.googleapis.com/css2?family=Saira:wght@400;600;700&display=swap">
<style>
  :root {
    --page-bg: #e6e9ee;
    --card-dark: #0b0b0f;
    --card-dark-2: #1c1c24;
    --frost-light: #eef2f6;
    --frost-mid: #c9d3de;
    --brand-yellow: #f2de2a;
    --brand-purple: #4b2f8c;
    --text-muted: #8d9ab3;
    --accent-orange: #d0893a;
    --arc-red: #d3261c;
    --arc-yellow: #f0d21e;
  }
  * { box-sizing: border-box; margin: 0; padding: 0; }
  html, body {
    width: 1200px; height: 900px; overflow: hidden;
    background: var(--page-bg);
    font-family: "Saira", sans-serif;
  }
  .card {
    position: absolute; left: 100px; top: 165px;
    width: 1000px; height: 570px;
    background: linear-gradient(135deg, var(--card-dark) 0%, var(--card-dark-2) 55%, var(--card-dark) 100%);
    box-shadow: 0 14px 40px rgba(0,0,0,0.25);
    overflow: hidden;
  }
  .card-art { position: absolute; inset: 0; }
  .brand-name {
    position: absolute; left: 56px; top: 52px;
    font-weight: 700; font-size: 92px; line-height: 1;
    letter-spacing: 3px; color: var(--brand-yellow);
  }
  .brand-sub {
    position: absolute; left: 58px; top: 148px;
    font-weight: 600; font-size: 36px; line-height: 1;
    color: var(--brand-purple);
  }
  .address {
    position: absolute; left: 56px; top: 310px;
    font-size: 25px; line-height: 32px; letter-spacing: 1px;
    color: var(--text-muted); font-style: normal;
  }
  .contact-list {
    position: absolute; left: 56px; top: 413px;
    list-style: none;
  }
  .contact-item {
    display: flex; align-items: center; gap: 10px;
    height: 33px;
    font-size: 24px; letter-spacing: 1px; color: var(--accent-orange);
  }
  .contact-item.email { color: var(--text-muted); font-size: 22px; }
  .contact-icon {
    width: 20px; height: 20px; flex: none;
    background: var(--accent-orange); border-radius: 2px;
    display: flex; align-items: center; justify-content: center;
  }
  .mark {
    position: absolute; left: 600px; top: 240px;
    display: flex; align-items: center; gap: 16px;
  }
  .mark-dot {
    width: 34px; height: 34px; border-radius: 50%;
    background: var(--brand-yellow);
  }
  .mark-name {
    font-weight: 700; font-size: 48px; line-height: 1;
    color: var(--brand-purple);
  }
</style>
</head>
<body>
  <div class="card">
    <svg class="card-art" width="1000" height="570" viewBox="0 0 1000 570">
      <defs>
        <linearGradient id="frost" x1="0" y1="0" x2="1" y2="1">
          <stop offset="0" stop-color="var(--frost-light)"/>
          <stop offset="1" stop-color="var(--frost-mid)"/>
        </linearGradient>
        <linearGradient id="arc" x1="0" y1="0" x2="0" y2="1">
          <stop offset="0" stop-color="var(--arc-red)"/>
          <stop offset="0.45" stop-color="var(--arc-yellow)"/>
          <stop offset="0.7" stop-color="var(--arc-yellow)"/>
          <stop offset="1" stop-color="var(--arc-red)"/>
        </linearGradient>
      </defs>
      <path role="img" aria-label="Clear frosted card panel"
            d="M780 0 C380 40 380 530 800 570 L1000 570 L1000 0 Z" fill="url(#frost)"/>
      <path d="M780 0 C380 40 380 530 800 570" fill="none" stroke="url(#arc)" stroke-width="5"/>
    </svg>

    <div class="brand-name">DALTON</div>
    <div class="brand-sub">POWER SUPPLY, INC</div>

    <address class="address">
      418 Maple Ridge Lane<br>
      Brookvale, NC 27514
    </address>

    <ul class="contact-list">
      <li class="contact-item">
        <span class="contact-icon">
          <svg width="14" height="14" viewBox="0 0 24 24"><path d="M6.6 10.8a15 15 0 0 0 6.6 6.6l2.2-2.2a1 1 0 0 1 1-.25 11.4 11.4 0 0 0 3.6.57 1 1 0 0 1 1 1V20a1 1 0 0 1-1 1A17 17 0 0 1 3 4a1 1 0 0 1 1-1h3.5a1 1 0 0 1 1 1c0 1.25.2 2.45.57 3.57a1 1 0 0 1-.25 1z" fill="#111"/></svg>
        </span>
        555-214-7630
      </li>
      <li class="contact-item">
        <span class="contact-icon">
          <svg width="14" height="14" viewBox="0 0 24 24"><rect x="6" y="3" width="12" height="6" fill="#111"/><rect x="3" y="10" width="18" height="8" rx="1" fill="#111"/><rect x="7" y="15" width="10" height="6" fill="#111"/></svg>
        </span>
        555-214-8842
      </li>
      <li class="contact-item email">
        <span class="contact-icon">
          <svg width="14" height="14" viewBox="0 0 24 24"><rect x="2" y="5" width="20" height="14" rx="1" fill="#111"/><path d="M3 6l9 7 9-7" fill="none" stroke="#d0893a" stroke-width="2"/></svg>
        </span>
        daltonpower@brightmail-example.net
      </li>
    </ul>

    <div class="mark">
      <span class="mark-dot"></span>
      <span class="mark-name">Dalton Power</span>
    </div>
  </div>
</body>
</html>
```